Investment Firm Needs a Business Card Design

Need a business card for a new professional services firm that provides financial planning and investment management. Design should communicate financial safety and innovation. The contact information that needs to be on card is under Must Haves.

Target Market(s)

Retail Public

Industry/Entity Type

Investment

Requirements
Must have
• The data that needs to appear is in quotations:
"Darren Whitcombe, RWA"
(RWA logo either below my name or near my name)

"4417 Marlowe Lane
Suite 305
St. Charles, IL 60389"

"800-547-3162" (office)
"630-924-7318" (cell)
"darren@ledgerbeacon.net" (email)
"www.LedgerBeacon.net"
Nice to have
• would like to have the tag line "Steady Horizon(r)" with registered trade mark somewhere on card, maybe on back.

```html
<!DOCTYPE html>
<html lang="en">
<head>
<meta charset="utf-8">
<title>Ledger Beacon – Business Card</title>
<link rel="stylesheet" href="https://fonts.googleapis.com/css2?family=Montserrat:wght@500;600;700&display=swap">
<style>
  :root {
    --navy: #2b3566;
    --green: #3a9a3f;
    --ink: #3a3a3a;
    --icon: #4a4a4a;
    --card: #ffffff;
    --backdrop: #e9eaee;
  }
  * { box-sizing: border-box; margin: 0; padding: 0; }
  html, body {
    width: 1200px; height: 900px; overflow: hidden;
    background: var(--backdrop);
    font-family: "Montserrat", sans-serif;
  }
  .canvas { position: relative; width: 1200px; height: 900px; }

  .card {
    position: absolute;
    left: 280px;
    width: 640px; height: 366px;
    background: var(--card);
    border-radius: 30px;
    overflow: hidden;
    box-shadow: 0 6px 22px rgba(30, 35, 60, 0.14);
  }
  .card--front { top: 60px; }
  .card--back  { top: 470px; }

  /* straight side band with accent rule */
  .side-band {
    position: absolute; left: 0; top: 0; bottom: 0;
    width: 96px; background: var(--navy);
  }
  .side-rule {
    position: absolute; left: 106px; top: 0; bottom: 0;
    width: 4px; background: var(--green);
  }

  /* brand lockup */
  .brand {
    position: absolute;
    display: flex; align-items: center;
    font-variant: small-caps;
    letter-spacing: 2px;
    color: var(--navy);
    font-weight: 600;
  }
  .brand__mark { background: var(--navy); flex: none; }
  .brand__divider { width: 2px; background: var(--navy); flex: none; }
  .brand__name { white-space: nowrap; line-height: 1; }

  .card--front .brand { left: 160px; top: 58px; }
  .card--front .brand__mark { width: 66px; height: 66px; }
  .card--front .brand__divider { height: 86px; margin: 0 14px 0 18px; }
  .card--front .brand__name { font-size: 34px; padding-top: 26px; }

  .card--back .brand { left: 0; right: 0; top: 140px; justify-content: center; flex-direction: column; }
  .card--back .brand__mark { width: 50px; height: 50px; margin-bottom: 14px; }
  .card--back .brand__name { font-size: 30px; }

  /* contact block */
  .contact {
    position: absolute; left: 140px; top: 196px;
    list-style: none;
    font-variant: small-caps;
    font-size: 12.5px; letter-spacing: 1.3px;
    color: var(--ink); font-weight: 500;
    line-height: 17px;
  }
  .contact__item { display: flex; align-items: flex-start; gap: 7px; }
  .contact__icon {
    flex: none; width: 13px; height: 13px; margin-top: 2px;
    border-radius: 50%; background: var(--icon);
    display: flex; align-items: center; justify-content: center;
  }
  .contact__icon svg { width: 9px; height: 9px; }

  /* holder */
  .holder {
    position: absolute; right: 40px; bottom: 28px;
    text-align: right;
    font-variant: small-caps;
    color: var(--ink); letter-spacing: 2.2px;
  }
  .holder__name { font-size: 17px; font-weight: 600; }
  .holder__title { font-size: 14px; font-weight: 500; margin-top: 2px; }
</style>
</head>
<body>
<main class="canvas">

  <section class="card card--front" aria-label="Business card front">
    <span class="side-band" aria-hidden="true"></span>
    <span class="side-rule" aria-hidden="true"></span>

    <div class="brand">
      <span class="brand__mark" aria-hidden="true"></span>
      <span class="brand__divider" aria-hidden="true"></span>
      <span class="brand__name">Ledger Beacon</span>
    </div>

    <ul class="contact">
      <li class="contact__item">
        <span class="contact__icon"><svg viewBox="0 0 10 10"><path d="M5 1 L9 5 H8 V9 H2 V5 H1 Z" fill="#fff"/></svg></span>
        <span>4417 Marlowe Lane, Suite 305,<br>St. Charles, IL 60389</span>
      </li>
      <li class="contact__item">
        <span class="contact__icon"><svg viewBox="0 0 10 10"><path d="M2 1 L4 1 L5 3 L4 4 Q5 6 6 6 L7 5 L9 6 L9 8 Q8 9 7 9 Q1 8 1 3 Q1 2 2 1 Z" fill="#fff"/></svg></span>
        <span>800-547-3162</span>
      </li>
      <li class="contact__item">
        <span class="contact__icon"><svg viewBox="0 0 10 10"><rect x="3" y="1" width="4" height="8" rx="1" fill="#fff"/></svg></span>
        <span>630-924-7318</span>
      </li>
      <li class="contact__item">
        <span class="contact__icon"><svg viewBox="0 0 10 10"><rect x="1.5" y="2.5" width="7" height="5" fill="#fff"/><path d="M1.5 2.5 L5 5.5 L8.5 2.5" fill="none" stroke="#4a4a4a" stroke-width="0.8"/></svg></span>
        <span>darren@ledgerbeacon.net</span>
      </li>
      <li class="contact__item">
        <span class="contact__icon"><svg viewBox="0 0 10 10"><circle cx="5" cy="5" r="3.6" fill="none" stroke="#fff" stroke-width="1"/><path d="M1.5 5 H8.5 M5 1.4 V8.6" stroke="#fff" stroke-width="0.8"/></svg></span>
        <span>www.LedgerBeacon.net</span>
      </li>
    </ul>

    <div class="holder">
      <p class="holder__name">Darren Whitcombe</p>
      <p class="holder__title">RWA</p>
    </div>
  </section>

  <section class="card card--back" aria-label="Business card back">
    <div class="brand">
      <span class="brand__mark" aria-hidden="true"></span>
      <span class="brand__name">Ledger Beacon</span>
    </div>
  </section>

</main>
</body>
</html>
```